Redesign of iOS App Lumo Tutor

Redesign of existing App Lumo Tutor, an app that helps learning Japanese Kanjis, Hiragana, Katakana.

The functionallity should remain the same as today: the app is free, you may download it at the app store. But: I like the design of my other apps better ;)

Target Market(s)

Students learning Japanese

Industry/Entity Type

Teacher

Font styles to use
Sans Serif

Requirements
Must have
• Lumo Tutor has 7 main screens, all screens has to be designed for iPhone and iPad: Main, Settings, Reading Tests, Writing Tests, Game, Paper Mode, Search
Nice to have
• I like the logo as it is today

```html
<!DOCTYPE html>
<html lang="en">
<head>
<meta charset="utf-8">
<title>Lumo Tutor – Writing Test</title>
<link rel="stylesheet" href="https://fonts.googleapis.com/css2?family=Montserrat:wght@300;400;500;700;800&family=Noto+Sans+JP:wght@400&display=swap">
<style>
:root{
  --crimson:#bb1a2d;
  --crimson-deep:#a8172a;
  --tile-line:rgba(255,255,255,.28);
  --white:#ffffff;
  --ink:#111111;
  --green:#2fc26b;
  --blue:#3a8fdb;
  --red:#e2483d;
  --teal:#1fbf9f;
  --muted:#c9c9c9;
  --icon:#666666;
  --label:#8a8a8a;
  --guide:#e2e2e2;
}
*{box-sizing:border-box;margin:0;padding:0}
html,body{width:675px;height:1200px;overflow:hidden;background:var(--white);font-family:"Montserrat",sans-serif}
.screen{position:relative;width:675px;height:1200px;overflow:hidden;background:var(--white)}

.status-bar{position:absolute;left:0;top:0;width:100%;height:45px;font-size:20px;color:#000}
.status-bar .carrier{position:absolute;left:23px;top:11px;display:flex;align-items:center;gap:6px;font-weight:400}
.status-bar .time{position:absolute;left:0;right:0;top:11px;text-align:center;font-weight:600}
.status-bar .battery{position:absolute;right:18px;top:14px}

.score-header{position:absolute;left:0;top:45px;width:100%;height:117px}
.back{position:absolute;left:31px;top:41px}
.counter{position:absolute;top:20px;width:120px;margin-left:-60px;text-align:center}
.counter .value{font-size:50px;font-weight:300;line-height:1}
.counter .label{font-size:12px;font-weight:400;letter-spacing:.5px;margin-top:5px}
.counter.correct{left:187px;color:var(--green)}
.counter.pending{left:337px;color:var(--blue)}
.counter.wrong{left:470px;color:var(--red)}
.skip{position:absolute;right:39px;top:40px;font-size:23px;font-weight:500;letter-spacing:1px;color:var(--muted);border-bottom:2px dashed var(--muted);line-height:1.05}

.test-area{position:absolute;left:0;top:162px;width:100%;height:930px;background:linear-gradient(to bottom,var(--crimson) 85%,var(--crimson-deep))}
.kanji-row{position:absolute;left:76px;top:63px;display:flex;gap:18px}
.tile{width:90px;height:90px;border-radius:12px;border:2px solid var(--tile-line);position:relative}
.tile.done{background:var(--white);border-color:var(--white)}
.tile .glyph{display:block;text-align:center;font-family:"Noto Sans JP",sans-serif;font-size:60px;line-height:88px;color:var(--teal)}
.tile .meaning{position:absolute;left:-10px;right:-10px;top:101px;text-align:center;color:var(--white);font-size:17px;font-weight:400}

.writing-pad{position:absolute;left:76px;top:228px;width:522px;height:504px;background:var(--white);border-radius:14px;overflow:hidden}
.guide-v{position:absolute;left:272px;top:0;width:2px;height:100%;background:var(--guide)}
.guide-h{position:absolute;left:0;top:256px;width:100%;height:2px;background:var(--guide)}
.strokes{position:absolute;left:60px;top:55px;width:420px;height:370px;background:radial-gradient(ellipse at center,rgba(17,17,17,.10),rgba(17,17,17,.02) 70%,transparent);border-radius:10px}

.actions{position:absolute;left:76px;top:759px;width:525px;display:flex;justify-content:space-between}
.btn{width:241px;height:71px;border-radius:7px;font-size:24px;font-weight:800;letter-spacing:.5px;display:flex;align-items:center;justify-content:center}
.btn.clear{border:2px solid var(--white);color:var(--white)}
.btn.verify{background:var(--white);color:var(--crimson)}

.tab-bar{position:absolute;left:0;top:1092px;width:100%;height:108px;background:var(--white)}
.tab{position:absolute;top:-26px;width:116px;margin-left:-58px;text-align:center}
.tab .bump{position:absolute;left:0;top:0;width:116px;height:116px;border-radius:50%;background:var(--white)}
.tab svg{position:relative;margin-top:40px}
.tab .name{position:relative;display:block;font-size:13px;font-weight:500;color:var(--label);margin-top:4px}
</style>
</head>
<body>
<div class="screen">
  <div class="status-bar">
    <div class="carrier">Carrier
      <svg width="22" height="16" viewBox="0 0 22 16"><path d="M1 5.5a14 14 0 0 1 20 0M4.5 9a9 9 0 0 1 13 0M8 12.5a4 4 0 0 1 6 0" fill="none" stroke="#000" stroke-width="2.4" stroke-linecap="round"/><circle cx="11" cy="14.5" r="1.3"/></svg>
    </div>
    <div class="time">1:23 PM</div>
    <svg class="battery" width="44" height="18" viewBox="0 0 44 18"><rect x="1" y="1" width="38" height="16" rx="3.5" fill="none" stroke="#000" stroke-width="1.5"/><rect x="3.5" y="3.5" width="33" height="11" rx="1.5"/><rect x="40.5" y="6" width="2.5" height="6" rx="1"/></svg>
  </div>

  <header class="score-header">
    <svg class="back" width="50" height="32" viewBox="0 0 50 32"><path d="M48 16H3M17 2 3 16l14 14" fill="none" stroke="#c9c9c9" stroke-width="3" stroke-linecap="round" stroke-linejoin="round"/></svg>
    <div class="counter correct"><div class="value">13</div><div class="label">CORRECT</div></div>
    <div class="counter pending"><div class="value">0</div></div>
    <div class="counter wrong"><div class="value">1</div><div class="label">WRONG</div></div>
    <div class="skip">SKIP</div>
  </header>

  <main class="test-area">
    <div class="kanji-row">
      <div class="tile done"><span class="glyph">江</span><span class="meaning">creek</span></div>
      <div class="tile"></div>
      <div class="tile"></div>
      <div class="tile"></div>
      <div class="tile"></div>
    </div>

    <div class="writing-pad">
      <div class="guide-v"></div>
      <div class="guide-h"></div>
      <div class="strokes" role="img" aria-label="Handwritten strokes of the kanji for creek drawn by the learner"></div>
    </div>

    <div class="actions">
      <div class="btn clear">CLEAR</div>
      <div class="btn verify">VERIFY</div>
    </div>
  </main>

  <nav class="tab-bar">
    <div class="tab" style="left:111px"><div class="bump"></div>
      <svg width="30" height="40" viewBox="0 0 30 40"><path d="M2 2h18l8 8v28H2z M20 2v8h8" fill="none" stroke="#666" stroke-width="1.6" stroke-linejoin="round"/><path d="M7 16h16M7 21h16M7 26h16M7 31h12" stroke="#666" stroke-width="1.4"/></svg>
      <span class="name">Paper</span></div>
    <div class="tab" style="left:259px"><div class="bump"></div>
      <svg width="40" height="40" viewBox="0 0 40 40"><path d="M4 14h8a4 4 0 1 1 8 0h8v8a4 4 0 1 1 0 8v8h-8a4 4 0 1 0-8 0H4v-8a4 4 0 1 0 0-8z" fill="none" stroke="#666" stroke-width="1.6" stroke-linejoin="round"/></svg>
      <span class="name">Game</span></div>
    <div class="tab" style="left:407px"><div class="bump"></div>
      <svg width="40" height="40" viewBox="0 0 40 40"><circle cx="16" cy="16" r="12" fill="none" stroke="#666" stroke-width="2"/><path d="M25 25l12 12" stroke="#666" stroke-width="2.4" stroke-linecap="round"/></svg>
      <span class="name">Search</span></div>
    <div class="tab" style="left:555px"><div class="bump"></div>
      <svg width="40" height="40" viewBox="0 0 40 40"><g fill="none" stroke="#666" stroke-width="1.8"><circle cx="20" cy="20" r="6"/><path d="M17 3h6l1 5 4 2 4-3 4 4-3 4 2 4 5 1v6l-5 1-2 4 3 4-4 4-4-3-4 2-1 5h-6l-1-5-4-2-4 3-4-4 3-4-2-4-5-1v-6l5-1 2-4-3-4 4-4 4 3 4-2z" stroke-linejoin="round"/></g></svg>
      <span class="name">Settings</span></div>
  </nav>
</div>
</body>
</html>
```